Exciting New Year's Eve Church Flyer for Watch Night Service

Need an eye catching, exciting New Year's Eve flyer for our church's watch night service. We are an exciting very energetic church. We like bold sharp colors. Must include verbiage but does not have to be in exact order.
Watch Night Service
If it had not been for the Lord
Harbor of Grace Community Church
482 Wexcombe St
Larkspur Vale
December 31, 2018
10:30 pm till midnight

Target Market(s)

19-40 demographich

Requirements
Must have
• bold colors
Should not have
• Should not be serious nor too literal. A cross is not needed

```html
<!DOCTYPE html>
<html lang="en">
<head>
<meta charset="UTF-8">
<title>Watch Night Service – Harbor of Grace Community Church</title>
<link href="https://fonts.googleapis.com/css2?family=Cinzel:wght@600&family=Oswald:wght@500;700&family=Great+Vibes&family=Open+Sans:wght@600;700&display=swap" rel="stylesheet">
<style>
  :root {
    --crimson: #8e1322;
    --maroon: #3a050c;
    --deep: #1c0205;
    --gold: #eebf62;
    --gold-light: #ffe3a0;
    --gold-dark: #b9842e;
    --white: #ffffff;
    --bar: #170205;
  }
  * { margin: 0; padding: 0; box-sizing: border-box; }
  html, body { width: 893px; height: 1200px; overflow: hidden; background: var(--deep); }
  .flyer {
    position: relative;
    width: 893px;
    height: 1200px;
    overflow: hidden;
    background: radial-gradient(ellipse at 50% 45%, var(--crimson) 0%, #5c0913 45%, var(--maroon) 75%, var(--deep) 100%);
    font-family: "Open Sans", sans-serif;
    color: var(--white);
  }
  .accent-lines { position: absolute; inset: 0; }
  .fireworks {
    position: absolute;
    border-radius: 50%;
    background: radial-gradient(circle, rgba(255,200,140,0.55) 0%, rgba(230,90,70,0.25) 40%, rgba(0,0,0,0) 70%);
  }
  .fireworks.left { left: 40px; top: 150px; width: 240px; height: 240px; }
  .fireworks.right { right: 40px; top: 240px; width: 200px; height: 200px; }
  .church-name {
    position: absolute;
    top: 78px; left: 0; right: 0;
    text-align: center;
    font-family: "Cinzel", serif;
    font-weight: 600;
    color: var(--gold);
  }
  .church-name .mark {
    display: block;
    width: 20px; height: 20px;
    margin: 0 auto 12px;
    border-radius: 50%;
    background: var(--gold);
  }
  .church-name .line-main { display: block; font-size: 48px; letter-spacing: 6px; line-height: 1; }
  .church-name .line-sub { display: block; font-size: 16px; letter-spacing: 3px; margin-top: 8px; }
  .clock {
    position: absolute;
    left: 136px; top: 270px;
    width: 620px; height: 620px;
    border-radius: 50%;
    border: 6px solid rgba(238,191,98,0.75);
    background: radial-gradient(circle, rgba(120,20,30,0.2) 0%, rgba(40,4,8,0.55) 70%, rgba(20,2,4,0.7) 100%);
  }
  .title {
    position: absolute;
    left: 0; right: 0;
    text-align: center;
    font-family: "Oswald", sans-serif;
    font-weight: 700;
    text-transform: uppercase;
    line-height: 1;
  }
  .title.watch { top: 575px; font-size: 105px; letter-spacing: 4px; color: var(--white); }
  .title.night {
    top: 680px; font-size: 200px; letter-spacing: 6px;
    background: linear-gradient(180deg, var(--gold-light) 0%, var(--gold) 55%, var(--gold-dark) 100%);
    -webkit-background-clip: text; background-clip: text; color: transparent;
  }
  .skyline {
    position: absolute;
    left: 0; right: 0; top: 860px; height: 70px;
    background: linear-gradient(180deg, rgba(200,60,70,0) 0%, rgba(170,40,55,0.55) 60%, rgba(60,6,12,0.4) 100%);
  }
  .title-script {
    position: absolute;
    left: 0; right: 0; top: 856px;
    text-align: center;
    font-family: "Great Vibes", cursive;
    font-size: 80px;
    color: var(--white);
    line-height: 1;
  }
  .tagline {
    position: absolute;
    left: 0; right: 0; top: 948px;
    text-align: center;
    font-weight: 700;
    font-size: 22px;
    line-height: 1.3;
  }
  .date {
    position: absolute;
    left: 0; right: 0; top: 1012px;
    text-align: center;
    font-family: "Oswald", sans-serif;
    font-weight: 700;
    font-size: 64px;
    letter-spacing: 2px;
    color: var(--gold);
    line-height: 1;
  }
  .time {
    position: absolute;
    left: 0; right: 0; top: 1088px;
    text-align: center;
    font-family: "Oswald", sans-serif;
    font-weight: 500;
    font-size: 28px;
    letter-spacing: 1px;
    color: var(--white);
    line-height: 1.2;
  }
  .address-bar {
    position: absolute;
    left: 196px; right: 196px; top: 1140px; height: 42px;
    border-radius: 21px;
    background: var(--bar);
    display: flex; align-items: center; justify-content: center;
    font-weight: 600;
    font-size: 15px;
    letter-spacing: 2px;
    color: var(--white);
  }
</style>
</head>
<body>
<main class="flyer">
  <div class="fireworks left" role="img" aria-label="Firework burst in gold and red"></div>
  <div class="fireworks right" role="img" aria-label="Firework burst in gold and red"></div>

  <div class="clock" role="img" aria-label="Large clock face with Roman numerals pointing near midnight"></div>

  <svg class="accent-lines" width="893" height="1200" viewBox="0 0 893 1200" aria-hidden="true">
    <g stroke="#eebf62" stroke-linecap="round">
      <line x1="740" y1="235" x2="893" y2="80" stroke-width="4"/>
      <line x1="770" y1="240" x2="893" y2="115" stroke-width="2"/>
      <line x1="0" y1="1040" x2="150" y2="890" stroke-width="4"/>
      <line x1="0" y1="1080" x2="130" y2="950" stroke-width="2"/>
    </g>
  </svg>

  <header class="church-name">
    <span class="mark"></span>
    <span class="line-main">HARBOR</span>
    <span class="line-sub">OF GRACE COMMUNITY CHURCH</span>
  </header>

  <h1 class="title watch">Watch</h1>
  <p class="title night">Night</p>
  <div class="skyline" role="img" aria-label="City skyline silhouette glowing in red"></div>
  <p class="title-script">Service</p>

  <p class="tagline">If it had not been for the Lord<br>Harbor of Grace Community Church</p>
  <p class="date">DECEMBER 31, 2018</p>
  <p class="time">10:30 PM TILL MIDNIGHT</p>
  <div class="address-bar">482 WEXCOMBE ST | LARKSPUR VALE</div>
</main>
</body>
</html>
```